Van and Ute Car wrap design

Looking for some funky ideas for a car wrap design for our product.
Us:
Solid Surface and engineered stone benchtop manufacturer for Kitchens, Bathrooms office fitouts and more

Suppliers: (could you maybe grab some of their logos to use)?
Brindlequarz
Veltarin
Zo-Pelt
Gorvamite
Quellarite
Baxwellite
Feldroy

Vehicles:
Korvanu E-vant 2012 (white)
Tavelonka Balsek 2018 (black)

Contact details:
sales@velmarobenchtops.com
www.velmarobenchtops.com
09 - 482 3915

Added some photos in and our logo. Would be good to see some options of what is possible?

```html
<!DOCTYPE html>
<html lang="en">
<head>
<meta charset="utf-8">
<title>Velmaro Benchtops – Van Wrap</title>
<link rel="stylesheet" href="https://fonts.googleapis.com/css2?family=Arimo:wght@400;700&display=swap">
<style>
  :root {
    --wrap-black: #050505;
    --wrap-grey: #a3a3a3;
    --wrap-blue: #2186d9;
    --brand-blue: #1b7fd6;
    --text-grey: #8c8c8c;
    --supplier-dark: #3a3a3a;
    --supplier-light: #ffffff;
    --supplier-red: #e0262b;
    --window: #1d1d1f;
    --tyre: #111111;
    --rim: #b9b5bd;
    --lamp-red: #c9232b;
    --lamp-clear: #dfe3e6;
    --page: #ffffff;
  }
  html, body { margin: 0; padding: 0; width: 1200px; height: 960px; overflow: hidden; background: var(--page); }
  .wrap-sheet { display: block; width: 1200px; height: 960px; }
  .url { font-family: "Arimo", Arial, sans-serif; font-weight: 700; font-size: 37px; fill: var(--text-grey); }
  .brand-name { font-family: "Arimo", Arial, sans-serif; font-weight: 700; fill: var(--brand-blue); }
  .brand-name--main { font-size: 130px; }
  .brand-name--sub { font-size: 58px; }
  .phone-number { font-family: "Arimo", Arial, sans-serif; font-weight: 700; font-size: 52px; fill: var(--wrap-black); }
  .email { font-family: "Arimo", Arial, sans-serif; font-weight: 400; font-size: 24px; fill: #ffffff; }
  .supplier { font-family: "Arimo", Arial, sans-serif; font-weight: 400; }
  .supplier--brindle { font-size: 27px; fill: var(--supplier-light); }
  .supplier--zopelt { font-size: 27px; fill: var(--supplier-light); }
  .supplier--gorva { font-size: 15px; fill: var(--supplier-dark); }
  .supplier--veltarin { font-size: 30px; fill: var(--supplier-dark); }
  .supplier--feldroy { font-size: 27px; fill: var(--supplier-red); }
  .body-black { fill: var(--wrap-black); }
  .body-grey { fill: var(--wrap-grey); }
  .body-blue { fill: var(--wrap-blue); }
  .window { fill: var(--window); }
  .wheel-arch { fill: var(--wrap-black); }
  .tyre { fill: var(--tyre); }
  .rim { fill: var(--rim); }
  .hub { fill: #8f8b94; }
  .lamp-rear { fill: var(--lamp-red); }
  .lamp-front { fill: var(--lamp-clear); }
  .ground-shadow { fill: #000; opacity: .55; }
  .social-dot { fill: var(--wrap-black); }
  .photo-frame { fill: var(--window); }
  .handle { fill: #1a1a1a; }
</style>
</head>
<body>
<svg class="wrap-sheet" viewBox="0 0 1500 1200" xmlns="http://www.w3.org/2000/svg">
  <defs>
    <clipPath id="van-body-clip">
      <path d="M58,430 L80,330 Q110,285 200,270 L330,240 Q480,110 640,62 L1380,38 Q1428,42 1440,120 L1452,430 L1446,522 L58,522 Z"/>
    </clipPath>
    <linearGradient id="g-kitchen" x1="0" y1="0" x2="1" y2="1">
      <stop offset="0" stop-color="#9a6c46"/><stop offset=".55" stop-color="#efe9e2"/><stop offset="1" stop-color="#c79a6c"/>
    </linearGradient>
    <linearGradient id="g-bathroom" x1="0" y1="0" x2="0" y2="1">
      <stop offset="0" stop-color="#d8d8d6"/><stop offset=".6" stop-color="#f1f1ef"/><stop offset="1" stop-color="#8f8c88"/>
    </linearGradient>
    <linearGradient id="g-cooktop" x1="0" y1="0" x2="1" y2="1">
      <stop offset="0" stop-color="#6b6b6b"/><stop offset=".5" stop-color="#2a2a2a"/><stop offset="1" stop-color="#d9d6d0"/>
    </linearGradient>
    <linearGradient id="g-benchtop" x1="0" y1="0" x2="1" y2="1">
      <stop offset="0" stop-color="#7d7f82"/><stop offset=".6" stop-color="#9da0a3"/><stop offset="1" stop-color="#8a6a4c"/>
    </linearGradient>
    <g id="van-body">
      <ellipse class="ground-shadow" cx="750" cy="580" rx="690" ry="6"/>
      <g clip-path="url(#van-body-clip)">
        <rect class="body-blue" x="0" y="0" width="1500" height="600"/>
        <rect class="body-black" x="0" y="0" width="1500" height="340"/>
        <path class="body-grey" d="M0,245 L600,256 L1500,280 L1500,336 L0,346 Z"/>
      </g>
      <path class="window" d="M335,236 Q470,120 640,80 L660,80 L655,236 Z"/>
      <rect class="handle" x="598" y="262" width="70" height="20" rx="6"/>
      <path class="lamp-front" d="M80,340 Q120,298 195,285 L170,370 Q110,385 78,380 Z"/>
      <path class="lamp-rear" d="M1388,200 Q1420,200 1422,250 L1420,345 Q1395,340 1378,300 Z"/>
      <circle class="wheel-arch" cx="265" cy="488" r="96"/>
      <circle class="wheel-arch" cx="1175" cy="488" r="96"/>
      <circle class="tyre" cx="265" cy="490" r="80"/>
      <circle class="rim" cx="265" cy="490" r="58"/>
      <circle class="hub" cx="265" cy="490" r="16"/>
      <circle class="tyre" cx="1175" cy="490" r="80"/>
      <circle class="rim" cx="1175" cy="490" r="58"/>
      <circle class="hub" cx="1175" cy="490" r="16"/>
    </g>
  </defs>

  <g class="van van--left">
    <use href="#van-body"/>
    <text class="url" x="765" y="72" textLength="568">www.velmarobenchtops.com</text>
    <text class="brand-name brand-name--main" x="765" y="214" textLength="588">VELMARO</text>
    <text class="brand-name brand-name--sub" x="767" y="268">BENCHTOPS</text>
    <path class="phone-icon" fill="#050505" d="M846,292 l12,-4 l10,18 l-8,7 q6,12 18,18 l7,-8 l17,10 l-4,12 q-36,2 -52,-53 Z"/>
    <text class="phone-number" x="905" y="327" textLength="400">09 - 482 3915</text>
    <circle class="social-dot" cx="1293" cy="383" r="19"/>
    <circle class="social-dot" cx="1341" cy="383" r="19"/>
    <circle class="social-dot" cx="1388" cy="383" r="19"/>
    <g class="suppliers">
      <text class="supplier supplier--brindle" x="240" y="280">Brindlequarz</text>
      <text class="supplier supplier--zopelt" x="448" y="280">Zo-Pelt</text>
      <text class="supplier supplier--gorva" x="187" y="320">GORVAMITE</text>
      <text class="supplier supplier--veltarin" x="300" y="324">Veltarin</text>
      <text class="supplier supplier--feldroy" x="468" y="320">Feldroy</text>
    </g>
    <g class="gallery">
      <rect class="photo-frame" x="364" y="342" width="720" height="160" rx="8"/>
      <rect x="372" y="349" width="168" height="148" rx="6" fill="url(#g-kitchen)" role="img" aria-label="Kitchen island with white stone benchtop and timber cabinetry"/>
      <rect x="552" y="349" width="166" height="120" rx="6" fill="url(#g-bathroom)" role="img" aria-label="Bathroom vanity with white benchtop and black basin"/>
      <rect x="730" y="349" width="168" height="120" rx="6" fill="url(#g-cooktop)" role="img" aria-label="Kitchen benchtop with gas cooktop"/>
      <rect x="910" y="349" width="168" height="142" rx="6" fill="url(#g-benchtop)" role="img" aria-label="Grey stone benchtop in a bar setting"/>
      <text class="email" x="552" y="492">sales@velmarobenchtops.com</text>
    </g>
  </g>

  <g class="van van--right">
    <use href="#van-body" transform="translate(1500,597) scale(-1,1)"/>
    <text class="url" x="165" y="670" textLength="568">www.velmarobenchtops.com</text>
    <text class="brand-name brand-name--main" x="153" y="808" textLength="588">VELMARO</text>
    <text class="brand-name brand-name--sub" x="155" y="862">BENCHTOPS</text>
    <path class="phone-icon" fill="#050505" d="M201,888 l12,-4 l10,18 l-8,7 q6,12 18,18 l7,-8 l17,10 l-4,12 q-36,2 -52,-53 Z"/>
    <text class="phone-number" x="265" y="925" textLength="400">09 - 482 3915</text>
    <circle class="social-dot" cx="110" cy="981" r="19"/>
    <circle class="social-dot" cx="157" cy="981" r="19"/>
    <circle class="social-dot" cx="205" cy="981" r="19"/>
    <g class="suppliers">
      <text class="supplier supplier--brindle" x="932" y="877">Brindlequarz</text>
      <text class="supplier supplier--zopelt" x="1140" y="877">Zo-Pelt</text>
      <text class="supplier supplier--gorva" x="880" y="918">GORVAMITE</text>
      <text class="supplier supplier--veltarin" x="1000" y="922">Veltarin</text>
      <text class="supplier supplier--feldroy" x="1162" y="917">Feldroy</text>
    </g>
    <g class="gallery">
      <rect class="photo-frame" x="418" y="939" width="716" height="158" rx="8"/>
      <rect x="425" y="945" width="165" height="142" rx="6" fill="url(#g-benchtop)" role="img" aria-label="Grey stone benchtop in a bar setting"/>
      <rect x="602" y="945" width="168" height="120" rx="6" fill="url(#g-cooktop)" role="img" aria-label="Kitchen benchtop with gas cooktop"/>
      <rect x="782" y="945" width="166" height="120" rx="6" fill="url(#g-bathroom)" role="img" aria-label="Bathroom vanity with white benchtop and black basin"/>
      <rect x="960" y="945" width="168" height="145" rx="6" fill="url(#g-kitchen)" role="img" aria-label="Kitchen island with white stone benchtop and timber cabinetry"/>
      <text class="email" x="600" y="1090">sales@velmarobenchtops.com</text>
    </g>
  </g>
</svg>
</body>
</html>
```